Business Card Design for Marketing Firm

Looking for business card design for higher end marketing firm. Clean but impressionable/trendy. We are a marketing firm that represents manufacturers in the foodservice equipment and supply industry. Our customers are end users such has hotels, restaurants, country clubs, convention centers and casinos as well as distributors of restaurants supplies and equipment, and manufacturers of foodservice equipment and supplies.
Target Market(s)
Hotels, Restaurants, Supply & Equipment Distributors, Foodservice Manufacturers
Industry/Entity Type
Foodservice/Hospitality
Contact Information for Business Card
Name, Title, Contact Number, Email, Website, Social Media, Address
Requirements
Must have
- Clean & Simple but Serious and Impressionable

```html
<!DOCTYPE html>
<html lang="en">
<head>
<meta charset="utf-8">
<title>Meridian Hospitality Reps – Business Card</title>
<link href="https://fonts.googleapis.com/css2?family=Figtree:wght@400;500;600;700&display=swap" rel="stylesheet">
<style>
  :root {
    --navy: #292b72;
    --ink-light: #ffffff;
    --page: #ffffff;
  }
  * { margin: 0; padding: 0; box-sizing: border-box; }
  html, body {
    width: 1200px; height: 1200px; overflow: hidden;
    background: var(--page);
    font-family: "Figtree", "Helvetica Neue", Arial, sans-serif;
    color: var(--ink-light);
  }
  .canvas { position: relative; width: 1200px; height: 1200px; }
  .card {
    position: absolute; width: 656px; height: 401px;
    background: var(--navy); overflow: hidden;
  }
  .card--front { left: 276px; top: 182px; }
  .card--back  { left: 275px; top: 624px; }

  /* front */
  .brand {
    position: absolute; left: 0; right: 0; top: 150px;
    display: flex; flex-direction: column; align-items: center; gap: 16px;
  }
  .brand__dot {
    width: 40px; height: 40px; border-radius: 50%;
    border: 2px solid var(--ink-light);
  }
  .brand__name {
    font-size: 22px; font-weight: 500; letter-spacing: 0.08em;
    text-transform: uppercase;
  }

  /* back */
  .person { position: absolute; left: 36px; top: 33px; }
  .person__name { font-size: 21px; font-weight: 700; line-height: 1.2; }
  .person__title { font-size: 17.5px; font-weight: 400; line-height: 1.3; margin-top: 1px; }

  .contacts {
    position: absolute; left: 36px; top: 164px;
    list-style: none; display: flex; flex-direction: column; gap: 7px;
  }
  .contacts__item {
    display: flex; align-items: center; gap: 12px;
    font-size: 16px; font-weight: 500; line-height: 19px;
  }
  .contacts__icon { width: 18px; height: 18px; flex: none; }

  .address {
    position: absolute; left: 36px; top: 299px;
    font-size: 15px; font-weight: 400; line-height: 20px; font-style: normal;
  }
  .website {
    position: absolute; left: 36px; top: 346px;
    font-size: 15px; font-weight: 600;
  }
</style>
</head>
<body>
<main class="canvas">
  <section class="card card--front" aria-label="Card front">
    <div class="brand">
      <span class="brand__dot" aria-hidden="true"></span>
      <span class="brand__name">Meridian Hospitality Reps</span>
    </div>
  </section>

  <section class="card card--back" aria-label="Card back">
    <div class="person">
      <h1 class="person__name">Rosalind Achterberg</h1>
      <p class="person__title">Chief Operation Marketing</p>
    </div>

    <ul class="contacts">
      <li class="contacts__item">
        <svg class="contacts__icon" viewBox="0 0 24 24" aria-hidden="true">
          <path fill="#fff" d="M6.6 10.8c1.4 2.8 3.8 5.1 6.6 6.6l2.2-2.2c.3-.3.7-.4 1-.2 1.1.4 2.3.6 3.6.6.6 0 1 .4 1 1V20c0 .6-.4 1-1 1C10.6 21 3 13.4 3 4c0-.6.4-1 1-1h3.5c.6 0 1 .4 1 1 0 1.3.2 2.5.6 3.6.1.3 0 .7-.2 1z"/>
        </svg>
        <span>+00 00 0000 0000</span>
      </li>
      <li class="contacts__item">
        <svg class="contacts__icon" viewBox="0 0 24 24" aria-hidden="true">
          <rect x="2" y="5" width="20" height="14" fill="none" stroke="#fff" stroke-width="1.6"/>
          <path d="M2 5l10 8 10-8M2 19l8-7M22 19l-8-7" fill="none" stroke="#fff" stroke-width="1.3"/>
        </svg>
        <span>rosalind.achterberg@meridianhospitality.com</span>
      </li>
      <li class="contacts__item">
        <svg class="contacts__icon" viewBox="0 0 24 24" aria-hidden="true">
          <rect x="3" y="3" width="18" height="18" fill="none" stroke="#fff" stroke-width="1.8"/>
        </svg>
        <span>@meridianreps</span>
      </li>
    </ul>

    <address class="address">
      2240 Harbor Lane Suite 310 Costa Mesa,<br>
      CA 92627 United States.
    </address>
    <p class="website">meridianhospitality.com</p>
  </section>
</main>
</body>
</html>
```